" A Empresa se chama Vento Sul Hotéis. Somos uma empresa do ramo hoteleiro. Esta é a marca da Holding que participa em todos os empreendimentos que administramos. Somos novos no mercado hoteleiro mas temos mais de 30 anos de tradiçao no mercado de construçao e imóveis. "

```html
<!DOCTYPE html>
<html lang="pt-BR">
<head>
<meta charset="UTF-8">
<title>Vento Sul Hotéis — Papel Timbrado</title>
<link rel="stylesheet" href="https://fonts.googleapis.com/css2?family=Montserrat:wght@500&display=swap">
<style>
  :root {
    --backdrop: #e6e4e1;
    --paper: #ffffff;
    --accent: #e8602c;
    --ink: #4a4a4a;
    --ink-soft: #7a7a7a;
  }
  * { margin: 0; padding: 0; box-sizing: border-box; }
  html, body {
    width: 1200px;
    height: 1200px;
    overflow: hidden;
    background: var(--backdrop);
  }
  .canvas {
    position: relative;
    width: 1200px;
    height: 1200px;
  }
  .letterhead {
    position: absolute;
    left: 204px;
    top: 40px;
    width: 792px;
    height: 1120px;
    background: var(--paper);
    box-shadow: 0 6px 24px rgba(0,0,0,0.18);
    font-family: "Montserrat", sans-serif;
  }
  .brand {
    position: absolute;
    top: 78px;
    left: 0;
    right: 0;
    display: flex;
    align-items: center;
    justify-content: center;
    gap: 14px;
  }
  .brand-square {
    width: 30px;
    height: 30px;
    background: var(--accent);
  }
  .brand-name {
    font-family: "Montserrat", sans-serif;
    font-weight: 500;
    font-size: 40px;
    letter-spacing: 1px;
    color: var(--ink);
  }
  .footer-rule {
    position: absolute;
    top: 1056px;
    width: 78px;
    height: 9px;
    background: var(--accent);
  }
  .footer-rule.left { left: 0; }
  .footer-rule.right { right: 0; }
  .contact {
    position: absolute;
    top: 1054px;
    left: 0;
    right: 0;
    text-align: center;
    font-size: 13px;
    line-height: 17px;
    color: var(--ink-soft);
  }
  .contact .site {
    color: var(--ink);
    font-weight: 500;
  }
</style>
</head>
<body>
<main class="canvas">
  <section class="letterhead">
    <header class="brand">
      <span class="brand-square"></span>
      <span class="brand-name">Vento Sul Hotéis</span>
    </header>

    <span class="footer-rule left"></span>
    <span class="footer-rule right"></span>

    <footer class="contact">
      <p class="address">Rua das Palmeiras, 220 - Sala 04, Jardim Primavera Niterói - RJ</p>
      <p class="phone-mail">Tel.: (21)4000-1234 - E-mail: contato@ventosulhoteis.com</p>
      <p class="site">www.ventosulhoteis.com</p>
    </footer>
  </section>
</main>
</body>
</html>
```